New Business Card Design Project for Handyman Business

I would like to purchase a customized version of a design you have previously submitted - https://www.plimvaro.example/work/58302716
I love this design!
I am hoping you can design something similar to this for our Handyman Business.
Attached is our logo and some graphics we have used.
Here is a link to the Google Doc with the content that needs to be included, https://files.trenowick.example/sheet/q/4XRKW-7hLp2DnQv8sTc5ma-ZzoeB3kWu9YyTgp6HJ__RmwNdVcQeLbs4jfnv0ztqxhaK7M41p9ggWHe/view
Target Market(s)
Real Estate Agents, Home Owners and Property Managers
Industry/Entity Type
Construction/ Speciality Trade
Contact Information for Business Card
https://files.trenowick.example/sheet/7QpaRzN_ukoyb4cXTwLHhJe8KnuSbPjCr2QDaLy6nwod/view?mode=shared
Font styles to use
Other font styles liked:
- Ubuntu
Look and feel
Each slider illustrates characteristics of the customer's brand and the style your logo design should communicate.

```html
<!DOCTYPE html>
<html lang="en">
<head>
<meta charset="utf-8">
<title>Fixwell Business Card</title>
<link href="https://fonts.googleapis.com/css2?family=Ubuntu:wght@400;500;700&display=swap" rel="stylesheet">
<style>
  :root {
    --backdrop: #969696;
    --brand-blue: #2277bb;
    --pattern-blue: #2a80c2;
    --brand-green: #4db848;
    --accent-orange: #e8703a;
    --white: #ffffff;
  }
  * { margin: 0; padding: 0; box-sizing: border-box; }
  html, body { width: 1200px; height: 1000px; overflow: hidden; }
  body {
    background: var(--backdrop);
    font-family: 'Ubuntu', sans-serif;
    position: relative;
    color: var(--white);
  }
  .card {
    position: absolute;
    top: 197px;
    width: 349px;
    height: 597px;
    border-radius: 20px;
    background: var(--brand-blue);
    overflow: hidden;
    text-align: center;
  }
  .card-front { left: 179px; }
  .card-back { left: 624px; }

  .brand-mark {
    position: absolute;
    left: 50%;
    transform: translateX(-50%);
    border-radius: 50%;
    background: var(--white);
  }
  .front-mark { top: 72px; width: 70px; height: 70px; }
  .brand-name {
    position: absolute;
    left: 0; right: 0;
    font-weight: 500;
    color: var(--white);
  }
  .front-name { top: 160px; font-size: 48px; line-height: 56px; }
  .brand-tagline {
    position: absolute;
    left: 0; right: 0;
    color: var(--accent-orange);
    font-weight: 500;
    letter-spacing: 2.4px;
    text-transform: uppercase;
  }
  .front-tagline { top: 213px; font-size: 13px; }

  .person-name { position: absolute; top: 290px; left: 0; right: 0; font-weight: 700; font-size: 23px; letter-spacing: 0.5px; }
  .person-role { position: absolute; top: 318px; left: 0; right: 0; font-size: 19px; color: var(--accent-orange); }
  .divider { position: absolute; top: 359px; left: 152px; width: 45px; height: 2px; background: var(--brand-green); }
  .contact-list { position: absolute; top: 383px; left: 0; right: 0; list-style: none; font-size: 19px; line-height: 24.5px; }

  .service-band {
    position: absolute;
    bottom: 0; left: 0; right: 0;
    height: 67px;
    background: var(--brand-green);
    font-size: 16px;
    line-height: 23px;
    padding-top: 10px;
  }
  .service-band .sep {
    display: inline-block;
    width: 6px; height: 6px;
    border-radius: 50%;
    background: var(--white);
    margin: 0 4px 3px;
    vertical-align: middle;
  }

  .back-pattern {
    position: absolute;
    inset: 0;
    background: linear-gradient(180deg, var(--pattern-blue), var(--brand-blue));
  }
  .back-brand { position: absolute; top: 438px; left: 0; right: 0; height: 52px; }
  .back-mark { top: 8px; left: 64px; transform: none; width: 34px; height: 34px; }
  .back-name { top: 0; left: 102px; right: auto; font-size: 34px; line-height: 40px; }
  .back-tagline { top: 38px; left: 126px; right: auto; font-size: 10px; letter-spacing: 1.4px; }
  .social-row {
    position: absolute;
    top: 500px; left: 0; right: 0;
    display: flex; justify-content: center; align-items: center; gap: 8px;
  }
  .social-row .rule { width: 38px; height: 2px; background: var(--white); margin: 0 5px; }
  .social-row .social-slot { width: 33px; height: 33px; border: 2px solid var(--white); border-radius: 50%; }
  .hashtag { position: absolute; top: 541px; left: 0; right: 0; font-size: 16px; }
</style>
</head>
<body>
  <section class="card card-front">
    <div class="brand-mark front-mark"></div>
    <div class="brand-name front-name">Fixwell</div>
    <div class="brand-tagline front-tagline">Home Care Specialists</div>

    <div class="person-name">REID CALLOWAY</div>
    <div class="person-role">Owner/ Handyman</div>
    <div class="divider"></div>
    <ul class="contact-list">
      <li>(555) 014-2277</li>
      <li>reid@fixwell-pro.example</li>
      <li>Fixwell-pro.example</li>
    </ul>

    <div class="service-band">
      <div>Commercial and Resdiential Handyman</div>
      <div>Improve<span class="sep"></span>Repair<span class="sep"></span>Remodel<span class="sep"></span>Maintain</div>
    </div>
  </section>

  <section class="card card-back">
    <div class="back-pattern" role="img" aria-label="Repeating pattern of faint brand marks across the card"></div>
    <div class="back-brand">
      <div class="brand-mark back-mark"></div>
      <div class="brand-name back-name">Fixwell</div>
      <div class="brand-tagline back-tagline">Home Care Specialists</div>
    </div>
    <div class="social-row">
      <span class="rule"></span>
      <span class="social-slot"></span>
      <span class="social-slot"></span>
      <span class="social-slot"></span>
      <span class="social-slot"></span>
      <span class="rule"></span>
    </div>
    <div class="hashtag">#FixwellHandymanServices</div>
  </section>
</body>
</html>
```